Marrowick Billboards

We already hava a logo, slogan and general theme, we are looking for 2 to 3 billboard designs for out Recreational-Use Retail Cannabis Dispensary in NY state. We would like for the billboard to be a "Space" theme with a realistic-looking astronaut, we cannot have any "cartoon-like" images that would be attractive to children per state regulations. We would like the following wording included:
Marrowick Cannabis Company - Oswego , slogan is "Products out of this world" , address of 871 Tallow Lane - Oswego, Free Delivery - Orders over $150 . Our primary brand color is lime green.

```html
<!DOCTYPE html>
<html lang="en">
<head>
<meta charset="utf-8">
<title>Marrowick Cannabis Company – Billboard</title>
<link rel="stylesheet" href="https://fonts.googleapis.com/css2?family=Bebas+Neue&family=Montserrat:wght@500;600;800&display=swap">
<style>
  :root {
    --lime: #9cf53a;
    --white: #ffffff;
    --space: #0d0f17;
    --space-mid: #14213a;
    --earth: #1d4f8c;
    --glow: #6fb4ff;
    --page: #c9c9c9;
  }
  * { margin: 0; padding: 0; box-sizing: border-box; }
  html, body { width: 881px; height: 1200px; overflow: hidden; }
  body {
    background: var(--page);
    font-family: "Montserrat", sans-serif;
    position: relative;
  }
  .billboard {
    position: absolute;
    left: 20px; top: 390px;
    width: 841px; height: 420px;
    background: var(--space);
    overflow: hidden;
    box-shadow: 6px 10px 24px rgba(0,0,0,0.45);
  }
  .billboard__scene {
    position: absolute; inset: 0;
    background:
      radial-gradient(ellipse 560px 150px at 640px 330px, rgba(111,180,255,0.55), transparent 70%),
      radial-gradient(ellipse 900px 260px at 620px 470px, var(--earth) 0%, #0f2a52 45%, transparent 75%),
      radial-gradient(ellipse 170px 230px at 670px 200px, #d9dde3 0%, #9aa1ab 45%, transparent 75%),
      linear-gradient(180deg, var(--space) 0%, var(--space-mid) 100%);
  }
  .brand {
    position: absolute; left: 0; width: 470px; top: 26px;
    text-align: center; color: var(--white);
    font-weight: 500; text-transform: uppercase;
  }
  .brand__name { font-size: 22px; letter-spacing: 1px; line-height: 1.15; }
  .brand__line { width: 210px; height: 1px; background: var(--white); margin: 6px auto 6px; }
  .brand__town { font-size: 16px; letter-spacing: 1px; }
  .slogan-frame {
    position: absolute; left: 68px; top: 137px;
    width: 338px; height: 150px;
    border: 1px solid rgba(255,255,255,0.8);
    border-radius: 4px;
  }
  .slogan__top, .slogan__main {
    position: absolute; left: 0; width: 470px; text-align: center;
    font-family: "Bebas Neue", sans-serif; line-height: 1;
  }
  .slogan__top {
    top: 114px; font-size: 52px; color: var(--white);
  }
  .slogan__top span, .address span { background: #101522; padding: 0 10px; }
  .slogan__main {
    top: 158px; font-size: 132px; color: var(--lime);
  }
  .address {
    position: absolute; left: 0; width: 470px; top: 277px;
    text-align: center; color: var(--white);
    font-size: 16px; font-weight: 600;
  }
  .address svg { vertical-align: -3px; margin-right: 4px; }
  .truck { position: absolute; left: 64px; top: 314px; }
  .delivery {
    position: absolute; left: 137px; top: 310px;
    text-transform: uppercase; line-height: 0.95;
  }
  .delivery__free { font-size: 38px; font-weight: 800; color: var(--lime); }
  .delivery__label { font-size: 20px; font-weight: 800; color: var(--white); }
  .delivery__sub { font-size: 13px; font-weight: 800; color: var(--white); }
  .price {
    position: absolute; left: 256px; top: 306px;
    font-family: "Bebas Neue", sans-serif; font-size: 106px; line-height: 1;
    color: var(--lime);
  }
</style>
</head>
<body>
  <section class="billboard">
    <div class="billboard__scene" role="img" aria-label="Photograph of an astronaut floating in space above the night side of Earth, city lights and a blue atmospheric glow on the horizon"></div>

    <header class="brand">
      <div class="brand__name">Marrowick<br>Cannabis Company</div>
      <div class="brand__line"></div>
      <div class="brand__town">Oswego</div>
    </header>

    <div class="slogan-frame"></div>
    <h1 class="slogan__top"><span>Out of this</span></h1>
    <div class="slogan__main">World</div>

    <p class="address"><span><svg width="12" height="16" viewBox="0 0 12 16"><path d="M6 0a6 6 0 0 0-6 6c0 4.5 6 10 6 10s6-5.5 6-10a6 6 0 0 0-6-6zm0 8.5A2.5 2.5 0 1 1 6 3.5a2.5 2.5 0 0 1 0 5z" fill="#9cf53a"/></svg>871 Tallow Lane - Oswego</span></p>

    <svg class="truck" width="62" height="82" viewBox="0 0 62 82" aria-hidden="true">
      <rect x="24" y="4" width="36" height="58" fill="#fff"/>
      <path d="M2 34 L10 18 H21 V62 H2 Z" fill="#fff"/>
      <rect x="8" y="22" width="9" height="12" fill="#0d0f17"/>
      <circle cx="14" cy="66" r="11" fill="#0d0f17"/>
      <circle cx="14" cy="66" r="8" fill="#fff"/>
      <circle cx="14" cy="66" r="3" fill="#0d0f17"/>
    </svg>

    <div class="delivery">
      <div class="delivery__free">Free</div>
      <div class="delivery__label">Delivery</div>
      <div class="delivery__sub">Orders over</div>
    </div>
    <div class="price">$150</div>
  </section>
</body>
</html>
```